Wedding Invitation for a wedding at home - personal, romantic event

Want a wedding invitation that is to be printed onto card.
Size to be 148mm x 210mm
For it to open like a book not tent card
Have a picture of a house that I want to be the front cover.
I've attached 2 pictures. I like the picture without the man but with the grass
For the photo to become a drawing and the colours to be brighter.
If you could use the picture of us and get us in one of the windows.
If you could put the picture of the dog maybe somewhere on the grass.
Love the colour of the sky in the picture of the beach

Words to be on the inside of the card:
Together with our families
You are invited to the Wedding Reception of Tessa Ormond and Rob Haskins
On Saturday 9th of September 2017 at 6pm
At Wexbury Lodge, 41b, Fenwold Crescent, Camberley, Surrey, GU19 7PW
Carriages at 1am
RSVP by Friday 27th of July to 07916 538 217

Words on the Back page:
With all that we have, we've been truly blessed.
Your presence and prayers are all that we request.
But if you desire to give nonetheless,
Monetary gift is one we suggest.

If the pages can be white.
Writing in gold
gold border on all pages

Target Market(s)

Wedding guests

Industry/Entity Type

Wedding

Font styles to use
Script

Requirements
Must have
• Romantic feel. Our wedding colours are white, gold and rose gold.
• Designer to be creative and I do not have much inspiration.
Nice to have
• metallic colours
• Maybe have MR & MRS in gold metallic on the front page

```html
<!DOCTYPE html>
<html lang="en">
<head>
<meta charset="utf-8">
<title>Tessa &amp; Rob – Wedding Invitation</title>
<link rel="stylesheet" href="https://fonts.googleapis.com/css2?family=Great+Vibes&family=Pinyon+Script&family=Cormorant+Garamond:wght@400;500&family=Tinos&display=swap">
<style>
  :root {
    --backdrop: #000000;
    --paper: #ffffff;
    --gold: #b8863b;
    --gold-light: #e2b85a;
    --gold-deep: #9c6b2c;
    --gold-pale: #efe2c8;
    --sky-warm: #f6dca0;
    --sky-cool: #c9cfd8;
    --brick: #b8755c;
    --lawn: #8f9a6a;
  }
  * { margin: 0; padding: 0; box-sizing: border-box; }
  html, body {
    width: 1113px; height: 1200px; overflow: hidden;
    background: var(--backdrop);
  }
  .canvas { position: relative; width: 1113px; height: 1200px; }

  .sheet { position: absolute; left: 172px; width: 755px; background: var(--paper); }
  .sheet--outer { top: 72px; height: 527px; }
  .sheet--inner { top: 625px; height: 527px; }

  .page { position: absolute; top: 4px; width: 368px; height: 517px; overflow: hidden; }
  .page--left { left: 7px; }
  .page--right { left: 382px; }
  .page__frame {
    position: absolute; inset: 0;
    border: 2px solid var(--gold);
    border-image: linear-gradient(135deg, var(--gold-deep), var(--gold-light) 40%, var(--gold) 70%, var(--gold-light)) 1;
    pointer-events: none; z-index: 5;
  }

  .gold-text {
    background: linear-gradient(100deg, var(--gold-deep), var(--gold) 45%, var(--gold-light) 100%);
    -webkit-background-clip: text; background-clip: text;
    color: transparent;
  }
  .serif { font-family: "Cormorant Garamond", serif; color: var(--gold); text-align: center; }

  /* Back page verse */
  .verse { position: absolute; top: 184px; left: 0; width: 100%; font-size: 15px; line-height: 17px; }
  .verse p + p { margin-top: 14px; }

  /* Cover */
  .cover__art {
    position: absolute; inset: 0 0 60px 0;
    background:
      linear-gradient(to bottom, rgba(255,255,255,0) 55%, #ffffff 92%),
      linear-gradient(to bottom, transparent 60%, var(--lawn) 78%, transparent 92%),
      radial-gradient(ellipse 55% 35% at 55% 62%, var(--brick) 0%, rgba(184,117,92,0.6) 55%, transparent 80%),
      linear-gradient(to bottom, #fbfaf6 0%, var(--sky-warm) 25%, var(--sky-cool) 45%, #d8d6cf 70%);
  }
  .cover__name { position: absolute; font-family: "Great Vibes", cursive; line-height: 1; }
  .cover__name--first { left: 56px; top: 38px; font-size: 78px; }
  .cover__amp { position: absolute; left: 138px; top: 70px; font-family: "Great Vibes", cursive; font-size: 96px; color: var(--gold-pale); opacity: 0.7; line-height: 1; }
  .cover__name--second { left: 156px; top: 116px; font-size: 66px; }
  .cover__request { position: absolute; top: 430px; left: 0; width: 100%; font-family: "Tinos", serif; font-size: 12px; line-height: 13px; color: var(--gold-deep); text-align: center; }
  .cover__title { position: absolute; top: 458px; left: 0; width: 100%; text-align: center; font-family: "Great Vibes", cursive; font-size: 50px; letter-spacing: 6px; line-height: 1; }

  /* Inside */
  .welcome { position: absolute; top: 62px; left: 0; width: 100%; text-align: center; font-family: "Pinyon Script", cursive; font-size: 22px; line-height: 26px; }
  .couple { position: absolute; top: 164px; left: 0; width: 100%; text-align: center; font-family: "Great Vibes", cursive; font-size: 38px; line-height: 40px; letter-spacing: 2px; }
  .details { position: absolute; top: 309px; left: 0; width: 100%; font-size: 13px; line-height: 14px; }
  .details p + p { margin-top: 14px; }
  .rsvp { position: absolute; top: 462px; left: 0; width: 100%; font-size: 13px; line-height: 15px; }
</style>
</head>
<body>
<main class="canvas">

  <section class="sheet sheet--outer">
    <article class="page page--left back-page">
      <div class="verse serif">
        <p>With all that we have, we've been truly blessed.<br>Your presence and prayers are all that we request.</p>
        <p>But if you desire to give nonetheless,<br>Monetary gift is one we suggest.</p>
      </div>
      <div class="page__frame"></div>
    </article>

    <article class="page page--right cover-page">
      <div class="cover__art" role="img" aria-label="Painted illustration of the couple's red-brick house under a warm sunset sky, trees and lawn around it"></div>
      <span class="cover__amp">&amp;</span>
      <h1 class="cover__name cover__name--first gold-text">Rob</h1>
      <h1 class="cover__name cover__name--second gold-text">Tessa</h1>
      <p class="cover__request">Request The Pleasure Of Your Company<br>To Celebrate Their</p>
      <h2 class="cover__title gold-text">Wedding</h2>
      <div class="page__frame"></div>
    </article>
  </section>

  <section class="sheet sheet--inner">
    <article class="page page--left blank-page">
      <div class="page__frame"></div>
    </article>

    <article class="page page--right invite-page">
      <p class="welcome gold-text">Together with our families<br>You are invited to the Wedding<br>Reception of</p>
      <h2 class="couple gold-text">Tessa Ormond<br>&amp;<br>Rob Haskins</h2>
      <div class="details serif">
        <p>On Saturday 9th of September 2017 at 6pm</p>
        <p>At Wexbury Lodge, 41b, Fenwold Crescent,<br>Camberley, Surrey, GU19 7PW</p>
        <p>Carriages at 1:am</p>
      </div>
      <p class="rsvp serif">RSVP by<br>Friday 27th of July to 07916 538 217</p>
      <div class="page__frame"></div>
    </article>
  </section>

</main>
</body>
</html>
```